Take my logo and make me some cool looking business cards

I've got a logo that we've trademarked so you can't change the logo but you can change it's color combo and find a fun way to incorporate it into a new business card design that is fresh, stylish, and can be applied to some cool medium cost materials (plastic, wood, metal, etc). Basically, we're looking for business cards that stand out in a good way.
Here's the logo we're currently using:
Thanks to everyone that has submitted designs. We've narrowed down to the top 4 designs and tried to eliminate old versions or designs that just didn't match our vision as quickly as we could. We don't plan on keeping this open for the full 9 days; we plan on selecting a design in the next 48 hours; with the goal of having something in the hands of a printer, preferably plastic printer, by Thursday AM Pacific Time.
Business
- must include our existing logo

```html
<!DOCTYPE html>
<html lang="en">
<head>
<meta charset="utf-8">
<title>Airvane Business Card</title>
<link rel="stylesheet" href="https://fonts.googleapis.com/css2?family=Arimo:wght@400;700&display=swap">
<style>
  :root {
    --page-bg: #e9e7ec;
    --card-black: #151618;
    --card-edge: #2a2b2e;
    --ink-white: #f4f3f1;
    --ink-grey: #c9c9cb;
  }
  html, body {
    margin: 0;
    padding: 0;
    width: 1200px;
    height: 765px;
    overflow: hidden;
    background: var(--page-bg);
  }
  .canvas {
    position: relative;
    width: 1200px;
    height: 765px;
    display: flex;
    align-items: center;
    justify-content: center;
  }
  .business-card {
    position: relative;
    width: 900px;
    height: 495px;
    background: var(--card-black);
    border: 2px solid var(--card-edge);
    border-radius: 34px;
    box-sizing: border-box;
    box-shadow: 0 18px 40px rgba(0, 0, 0, 0.18);
  }
  .wordmark {
    position: absolute;
    top: 120px;
    left: 0;
    right: 0;
    margin: 0;
    text-align: center;
    font-family: "Arimo", Arial, sans-serif;
    font-weight: 400;
    font-size: 104px;
    letter-spacing: 6px;
    line-height: 1;
    color: var(--ink-white);
  }
  .contact {
    position: absolute;
    top: 308px;
    left: 0;
    right: 0;
    margin: 0;
    text-align: center;
    font-family: "Arimo", Arial, sans-serif;
    font-weight: 700;
    font-size: 17px;
    line-height: 1.5;
    letter-spacing: 0.6px;
    text-transform: uppercase;
    color: var(--ink-grey);
    font-style: normal;
  }
  .contact span { display: block; }
</style>
</head>
<body>
  <main class="canvas">
    <article class="business-card">
      <h1 class="wordmark">AIRVANE</h1>
      <address class="contact">
        <span class="contact-name">Jordan Hale, CEO</span>
        <span class="contact-address">418 Harbor Lane • Coral Bay, CA 90000</span>
        <span class="contact-lines">+15550123456 • jh@airvane.com</span>
      </address>
    </article>
  </main>
</body>
</html>
```